Packaging Design for a Quenby sweets company.

We need a packaging design for a new company based in Kuwait named Quenby. We sell trifles in mini sizes and large sizes. (google what a trifle looks like)

I've already attached what the box looks like along with the layouts. All that is needed is drawing on the box.

It Company

• Must have Instagram and Whatsapp/phone number on the box.

Instagram account: quenby_z4
whatsapp/phone: 95318460

```html
<!DOCTYPE html>
<html lang="en">
<head>
<meta charset="utf-8">
<title>Quenby – Box Packaging</title>
<link rel="stylesheet" href="https://fonts.googleapis.com/css2?family=Cormorant+Garamond:wght@500&family=Arimo:wght@400&display=swap">
<style>
  :root {
    --paper: #ffffff;
    --dieline: #e7b9cc;
    --pink-light: #eec3d8;
    --pink-mid: #e3a4c3;
    --pink-deep: #d889b0;
    --ribbon-edge: #a9b8e6;
    --ribbon-top: #6fc3c6;
    --ribbon-bottom: #a8dcdc;
    --label-cream: #f4f0e2;
    --stitch: #c68fc3;
    --brand-grey: #8d8d8d;
    --tag-lilac: #a9a3e0;
    --tag-field: #e9e7f7;
    --tag-ink: #333344;
    --string: #444444;
  }
  html, body {
    margin: 0;
    padding: 0;
    width: 1200px;
    height: 972px;
    overflow: hidden;
    background: var(--paper);
  }
  .box-net {
    display: block;
    width: 1200px;
    height: 972px;
  }
  .dieline { fill: none; stroke: var(--dieline); stroke-width: 1; }
  .brand-name {
    font-family: "Cormorant Garamond", serif;
    font-weight: 500;
    font-size: 66px;
    letter-spacing: 14px;
    fill: var(--brand-grey);
  }
  .tag-text {
    font-family: "Arimo", sans-serif;
    font-size: 11px;
    fill: var(--tag-ink);
  }
</style>
</head>
<body>
<svg class="box-net" viewBox="0 0 1200 972" xmlns="http://www.w3.org/2000/svg">
  <defs>
    <linearGradient id="panel-fill" x1="0" y1="0" x2="1" y2="0">
      <stop offset="0" stop-color="var(--pink-light)"/>
      <stop offset="0.5" stop-color="var(--pink-mid)"/>
      <stop offset="1" stop-color="var(--pink-light)"/>
    </linearGradient>
    <linearGradient id="ribbon-fill" x1="0" y1="0" x2="0" y2="1">
      <stop offset="0" stop-color="var(--ribbon-top)"/>
      <stop offset="1" stop-color="var(--ribbon-bottom)"/>
    </linearGradient>
    <filter id="soft-shadow" x="-10%" y="-10%" width="120%" height="130%">
      <feDropShadow dx="0" dy="4" stdDeviation="5" flood-color="#000" flood-opacity="0.25"/>
    </filter>
  </defs>

  <!-- Glue flaps and dieline -->
  <g class="flaps">
    <path class="dieline" d="M100 52 H1085"/>
    <path class="dieline" d="M70 160 V80 H162 M1020 80 H1110 V160"/>
    <path class="dieline" d="M80 180 L52 205 V770 L80 795 M1105 180 L1130 205 V770 L1105 795"/>
    <path class="dieline" d="M70 795 V875 H162 M1020 875 H1110 V795"/>
    <path class="dieline" d="M100 900 H1085"/>
  </g>

  <!-- Pink patterned panels -->
  <g class="panels" role="img" aria-label="Pink vertical stripe and polka dot pattern covering the box panels">
    <rect x="162" y="52" width="858" height="108" fill="url(#panel-fill)"/>
    <rect x="80" y="160" width="1025" height="635" fill="url(#panel-fill)"/>
    <rect x="162" y="795" width="858" height="105" fill="url(#panel-fill)"/>
    <path d="M162 160 V795 M1020 160 V795" stroke="var(--pink-deep)" stroke-opacity="0.4" fill="none"/>
  </g>

  <!-- Ribbon band -->
  <g class="ribbon">
    <rect x="80" y="395" width="1025" height="17" fill="var(--ribbon-edge)"/>
    <rect x="80" y="412" width="1025" height="135" fill="url(#ribbon-fill)"/>
    <rect x="80" y="547" width="1025" height="18" fill="var(--ribbon-edge)"/>
  </g>

  <!-- Label plaque -->
  <g class="label" filter="url(#soft-shadow)">
    <path fill="var(--label-cream)"
      d="M387 367 H480 Q605 285 730 367 H825 V415 Q915 478 825 540 V590 H730 Q605 680 480 590 H387 V540 Q295 478 387 415 Z"/>
  </g>
  <path class="label-stitch" fill="none" stroke="var(--stitch)" stroke-width="2" stroke-dasharray="7 5"
    d="M400 380 H485 Q605 305 725 380 H812 V422 Q890 478 812 533 V577 H725 Q605 660 485 577 H400 V533 Q320 478 400 422 Z"/>
  <text class="brand-name" x="612" y="568" text-anchor="middle">quenby</text>

  <!-- Contact tag -->
  <g class="contact-tag">
    <path d="M935 602 Q930 570 955 560 Q975 565 962 590" fill="none" stroke="var(--string)" stroke-width="1.2"/>
    <g transform="rotate(-10 888 640)" filter="url(#soft-shadow)">
      <rect x="830" y="608" width="116" height="64" rx="8" fill="var(--tag-lilac)"/>
      <circle cx="932" cy="618" r="3" fill="var(--paper)"/>
      <rect x="842" y="620" width="14" height="14" rx="3" fill="var(--tag-ink)"/>
      <rect x="860" y="620" width="62" height="14" fill="var(--tag-field)"/>
      <text class="tag-text" x="863" y="631">quenby_z4</text>
      <circle cx="849" cy="651" r="7" fill="var(--tag-ink)"/>
      <rect x="860" y="644" width="62" height="14" fill="var(--tag-field)"/>
      <text class="tag-text" x="863" y="655">95318460</text>
    </g>
  </g>
</svg>
</body>
</html>
```